Investment Business - Biz Card Design

Using the attached logo files, please create a superior business card design for Brantwell Holdings.

The "back" of the card should feature the logo (either in colour, or white/black over a feature colour)

The "front" of the card should feature: name, email, and phone

The design should be minimal and clean.

Target Market(s)

Business owners who need our investment services.

Industry/Entity Type

Business

```html
<!DOCTYPE html>
<html lang="en">
<head>
<meta charset="utf-8">
<title>Brantwell Holdings – Business Card</title>
<link rel="stylesheet" href="https://fonts.googleapis.com/css2?family=Michroma&family=Tinos&display=swap">
<style>
  :root {
    --page: #ffffff;
    --card-dark: #141414;
    --card-mid: #2c2c2c;
    --name-blue: #1a6ee8;
    --text-white: #f4f4f4;
    --mark-grey: #5c5c5c;
    --brand-blue: #3343b0;
    --brand-cyan: #3fb3e0;
    --tile-top: #fafafa;
    --tile-bottom: #d4d4d4;
    --icon-blue: #1d4f9a;
  }
  html, body {
    margin: 0;
    padding: 0;
    width: 1200px;
    height: 1000px;
    overflow: hidden;
    background: var(--page);
  }
  .canvas {
    position: relative;
    width: 1200px;
    height: 1000px;
  }
  .card {
    position: absolute;
    overflow: hidden;
    background:
      radial-gradient(ellipse at 50% 45%, var(--card-mid) 0%, var(--card-dark) 75%),
      var(--card-dark);
  }
  .card--front {
    left: 20px;
    top: 138px;
    width: 549px;
    height: 341px;
  }
  .card--back {
    left: 598px;
    top: 512px;
    width: 572px;
    height: 356px;
  }
  .holder-name {
    position: absolute;
    left: 50px;
    top: 30px;
    margin: 0;
    font-family: "Michroma", sans-serif;
    font-variant: small-caps;
    font-size: 26px;
    font-weight: 400;
    letter-spacing: 1px;
    color: var(--name-blue);
  }
  .contact-row {
    position: absolute;
    left: 52px;
    display: flex;
    align-items: center;
    gap: 18px;
  }
  .contact-row--email { top: 93px; }
  .contact-row--phone { top: 182px; }
  .icon-tile {
    width: 48px;
    height: 48px;
    border-radius: 8px;
    background: linear-gradient(var(--tile-top), var(--tile-bottom));
    box-shadow: 0 2px 3px rgba(0,0,0,0.6);
    display: flex;
    align-items: center;
    justify-content: center;
  }
  .contact-email {
    font-family: "Tinos", serif;
    font-size: 27px;
    color: var(--text-white);
  }
  .contact-phone {
    font-family: "Michroma", sans-serif;
    font-size: 17px;
    letter-spacing: 2px;
    color: var(--text-white);
  }
  .front-wordmark {
    position: absolute;
    right: 30px;
    bottom: 26px;
    font-family: "Michroma", sans-serif;
    font-size: 15px;
    color: var(--mark-grey);
    letter-spacing: 1px;
  }
  .back-brand {
    position: absolute;
    left: 0;
    right: 0;
    top: 0;
    bottom: 0;
    display: flex;
    align-items: center;
    justify-content: center;
    gap: 16px;
  }
  .brand-square {
    width: 30px;
    height: 30px;
    background: var(--brand-blue);
  }
  .brand-name {
    font-family: "Michroma", sans-serif;
    font-size: 25px;
    letter-spacing: 1px;
    color: var(--brand-blue);
  }
</style>
</head>
<body>
<div class="canvas">

  <section class="card card--front" aria-label="Card front">
    <h1 class="holder-name">Rohan Delwatte</h1>

    <div class="contact-row contact-row--email">
      <span class="icon-tile">
        <svg width="34" height="26" viewBox="0 0 34 26" aria-hidden="true">
          <rect x="1" y="1" width="32" height="24" fill="#fff" stroke="var(--icon-blue)" stroke-width="2"/>
          <polyline points="1,1 17,15 33,1" fill="none" stroke="var(--icon-blue)" stroke-width="2"/>
          <polyline points="1,25 13,12 M21,12 33,25" fill="none" stroke="var(--icon-blue)" stroke-width="1.5"/>
        </svg>
      </span>
      <span class="contact-email">info@brantwell.com</span>
    </div>

    <div class="contact-row contact-row--phone">
      <span class="icon-tile">
        <svg width="34" height="30" viewBox="0 0 34 30" aria-hidden="true">
          <path d="M2 9 Q17 -1 32 9 L29 13 L23 11 L23 8 Q17 6 11 8 L11 11 L5 13 Z" fill="var(--icon-blue)"/>
          <path d="M8 14 L26 14 L30 28 L4 28 Z" fill="var(--icon-blue)"/>
          <g fill="#fff">
            <rect x="12" y="17" width="2" height="2"/><rect x="16" y="17" width="2" height="2"/><rect x="20" y="17" width="2" height="2"/>
            <rect x="12" y="21" width="2" height="2"/><rect x="16" y="21" width="2" height="2"/><rect x="20" y="21" width="2" height="2"/>
          </g>
        </svg>
      </span>
      <span class="contact-phone">+94 71 4830517</span>
    </div>

    <div class="front-wordmark">Brantwell Holdings</div>
  </section>

  <section class="card card--back" aria-label="Card back">
    <div class="back-brand">
      <span class="brand-square"></span>
      <span class="brand-name">BRANTWELL HOLDINGS</span>
    </div>
  </section>

</div>
</body>
</html>
```